Small but growing painting company. Have built up a steady client base. Want to start having a more professional look. Want to start with changing my business cards, and also getting new logo and tee shirts.

Target Market(s)

Home owners, property management companies, all ages 30-70

Industry/Entity Type

Painting And Decorating

Contact Information for Business Card

Bright Ridge Painting LLC Mark Delvecchi 630-584-3907 interior, exterior, vaulted ceiling, drywall repair, pressure washing, kitchen cabinets, epoxy, garage floors,

Font styles to use
Sans Serif
Other font styles liked:
• Harrington

Colors
0355a3
ffffff
ec1f27
000000
3176b5
0493ce
474747
b7b7b7

Requirements
Must have
• Creative, something that doesn’t look like every other painting card.
Nice to have
• I would like something with an arrow or something going to a point

```html
<!DOCTYPE html>
<html lang="en">
<head>
<meta charset="utf-8">
<title>Bright Ridge Painting LLC – Business Card</title>
<link rel="stylesheet" href="https://fonts.googleapis.com/css2?family=Montserrat:wght@800&family=Roboto:wght@400;500;700&display=swap">
<style>
  :root {
    --stage: #1b1b1b;
    --card: #141414;
    --card-edge: #232323;
    --red: #ec1f27;
    --blue: #0493ce;
    --orange: #f7941d;
    --yellow: #ffe600;
    --white: #ffffff;
    --grey: #b7b7b7;
    --faint: #262626;
  }
  * { margin: 0; padding: 0; box-sizing: border-box; }
  html, body { width: 1200px; height: 1200px; overflow: hidden; background: var(--stage); }
  body { font-family: "Roboto", Arial, sans-serif; color: var(--white); position: relative; }

  .card {
    position: absolute; left: 150px; width: 900px; height: 514px;
    background: var(--card); border-radius: 22px; overflow: hidden;
    border: 1px solid var(--card-edge);
  }
  .card--back { top: 70px; }
  .card--front { top: 616px; }

  /* back */
  .back-ring {
    position: absolute; right: -60px; top: 40px; width: 430px; height: 430px;
    border: 70px solid var(--faint); border-radius: 50%;
  }
  .back-brand {
    position: absolute; left: 0; right: 0; top: 0; bottom: 0;
    display: flex; align-items: center; justify-content: center; gap: 26px;
  }
  .brand-dot {
    width: 120px; height: 120px; border-radius: 50%; background: var(--red); flex: none;
  }
  .back-brand .brand-name {
    font-family: "Montserrat", Arial, sans-serif; font-weight: 800;
    color: var(--red); font-size: 34px; line-height: 1.05; text-transform: uppercase;
  }

  /* front */
  .front-title {
    position: absolute; left: 70px; top: 58px;
    font-family: "Montserrat", Arial, sans-serif; font-weight: 800;
    color: var(--red); font-size: 52px; line-height: 1; text-transform: uppercase;
  }
  .front-dot {
    position: absolute; right: 70px; top: 60px; width: 170px; height: 170px;
    border-radius: 50%; background: var(--red);
  }
  .holder-name {
    position: absolute; left: 70px; top: 228px;
    font-weight: 700; font-size: 26px; letter-spacing: 0.5px; text-transform: uppercase;
  }
  .divider { position: absolute; left: 70px; right: 70px; height: 2px; background: var(--grey); }
  .divider--top { top: 276px; width: 360px; }
  .divider--contact { top: 378px; left: 520px; }

  .contact {
    position: absolute; right: 70px; top: 296px; text-align: right;
    font-size: 21px; line-height: 34px;
  }
  .contact-row { display: flex; align-items: center; justify-content: flex-end; gap: 12px; }
  .contact-row svg { width: 20px; height: 20px; flex: none; }

  .services {
    position: absolute; left: 70px; right: 70px; top: 296px;
    display: grid; grid-template-columns: repeat(4, auto); justify-content: space-between;
    font-size: 21px; line-height: 31px;
  }
  .services-col { list-style: none; }
  .services-col--1 { margin-top: 0; }
  .services-col--2 { margin-top: 26px; }
  .services-col--3 { margin-top: 100px; }
  .services-col--4 { margin-top: 100px; }
  .service { display: flex; align-items: center; gap: 10px; }
  .service svg { width: 14px; height: 14px; flex: none; }
  .contact { z-index: 1; }

  .front-band {
    position: absolute; left: 0; right: 0; bottom: 0; height: 14px;
    background: linear-gradient(90deg, var(--red), var(--orange) 45%, var(--yellow));
  }
</style>
</head>
<body>

<section class="card card--back">
  <div class="back-ring" aria-hidden="true"></div>
  <div class="back-brand">
    <span class="brand-dot" aria-hidden="true"></span>
    <span class="brand-name">Bright Ridge<br>Painting LLC</span>
  </div>
</section>

<section class="card card--front">
  <h1 class="front-title">Bright Ridge<br>Painting LLC</h1>
  <span class="front-dot" aria-hidden="true"></span>
  <p class="holder-name">Mark Delvecchi</p>
  <span class="divider divider--top"></span>

  <div class="contact">
    <div class="contact-row">630-584-3907
      <svg viewBox="0 0 24 24" aria-hidden="true"><path fill="#f7941d" d="M6.6 10.8a15 15 0 0 0 6.6 6.6l2.2-2.2c.3-.3.7-.4 1-.2 1.1.4 2.3.6 3.6.6.6 0 1 .4 1 1V20c0 .6-.4 1-1 1A17 17 0 0 1 3 4c0-.6.4-1 1-1h3.5c.6 0 1 .4 1 1 0 1.3.2 2.5.6 3.6.1.3 0 .7-.2 1z"/></svg>
    </div>
    <div class="contact-row">info@brightridgepainting.com
      <svg viewBox="0 0 24 24" aria-hidden="true"><rect x="2" y="5" width="20" height="14" rx="1" fill="#f7941d"/><path d="M2 6l10 7 10-7" fill="none" stroke="#ec1f27" stroke-width="1.6"/></svg>
    </div>
  </div>
  <span class="divider divider--contact"></span>

  <div class="services">
    <ul class="services-col services-col--1">
      <li class="service"><svg viewBox="0 0 14 14" aria-hidden="true"><path d="M2 12L12 2M12 2H6M12 2v6" stroke="#f7941d" stroke-width="2.4" fill="none"/></svg>Pressure washing</li>
      <li class="service"><svg viewBox="0 0 14 14" aria-hidden="true"><path d="M2 12L12 2M12 2H6M12 2v6" stroke="#f7941d" stroke-width="2.4" fill="none"/></svg>Kitchen cabinets</li>
    </ul>
    <ul class="services-col services-col--2">
      <li class="service"><svg viewBox="0 0 14 14" aria-hidden="true"><path d="M2 12L12 2M12 2H6M12 2v6" stroke="#f7941d" stroke-width="2.4" fill="none"/></svg>Epoxy</li>
      <li class="service"><svg viewBox="0 0 14 14" aria-hidden="true"><path d="M2 12L12 2M12 2H6M12 2v6" stroke="#f7941d" stroke-width="2.4" fill="none"/></svg>Garage floors</li>
    </ul>
    <ul class="services-col services-col--3">
      <li class="service"><svg viewBox="0 0 14 14" aria-hidden="true"><path d="M2 12L12 2M12 2H6M12 2v6" stroke="#f7941d" stroke-width="2.4" fill="none"/></svg>Interior</li>
      <li class="service"><svg viewBox="0 0 14 14" aria-hidden="true"><path d="M2 12L12 2M12 2H6M12 2v6" stroke="#f7941d" stroke-width="2.4" fill="none"/></svg>Exterior</li>
    </ul>
    <ul class="services-col services-col--4">
      <li class="service"><svg viewBox="0 0 14 14" aria-hidden="true"><path d="M2 12L12 2M12 2H6M12 2v6" stroke="#f7941d" stroke-width="2.4" fill="none"/></svg>Vaulted ceiling</li>
      <li class="service"><svg viewBox="0 0 14 14" aria-hidden="true"><path d="M2 12L12 2M12 2H6M12 2v6" stroke="#f7941d" stroke-width="2.4" fill="none"/></svg>Drywall repair</li>
    </ul>
  </div>

  <span class="front-band" aria-hidden="true"></span>
</section>

</body>
</html>
```